Brivolan - presentation for a remote DBA team offering data platform management

We need a website design for wordpress site called Brivolan.cz
We deliver remote database and data platform administration and development, oversee the database administrators, consult and train the personnel responsible for the database operations. The website should include several sections, home page with graphics elements supporting the name and service - remote dba work; blog section; service introduction and description, team introduction and description, download section for documents, presentations etc.

Target Market(s)

small and medium business companies requiring remote DBA service

Number of Pages Required

3 page

Font styles to use
Sans Serif

Colors

Designer to choose colors to be used in the design.

Requirements
Must have
• The website should have several sections to introduce the services, blog, team introduction, downloads

```html
<!DOCTYPE html>
<html lang="en">
<head>
<meta charset="utf-8">
<title>Brivolan – Data Platform Management</title>
<link href="https://fonts.googleapis.com/css2?family=Poppins:wght@400;500;600;700&family=Open+Sans:ital,wght@0,400;0,600;1,400&display=swap" rel="stylesheet">
<style>
:root{
  --navy:#0b1e78;
  --deep:#06104f;
  --royal:#1a5fd6;
  --sky:#1e90f0;
  --azure:#2196f3;
  --ink:#222a3a;
  --muted:#555d6e;
  --pale:#d7e9f5;
  --light:#f2f3f6;
  --white:#ffffff;
  --star:#f5a623;
}
*{box-sizing:border-box;margin:0;padding:0}
html,body{width:1200px;height:3974px;overflow:hidden;background:var(--white)}
body{font-family:"Open Sans",Arial,sans-serif;color:var(--ink);position:relative}
.abs{position:absolute}
h1,h2,h3{font-family:"Poppins",Arial,sans-serif;font-weight:500}

/* Header / hero */
.hero{left:0;top:0;width:1200px;height:720px;background:radial-gradient(ellipse at 20% 30%,#2a7cff 0%,#1533b8 30%,#0a1670 65%,#050c45 100%)}
.hero-glow{left:600px;top:250px;width:600px;height:300px;background:radial-gradient(ellipse,rgba(60,160,255,.55),transparent 70%)}
.brand{left:126px;top:28px;font-family:"Poppins",sans-serif;font-size:34px;color:var(--white);font-weight:500}
.nav{left:394px;top:34px;display:flex;gap:36px;font-family:"Poppins",sans-serif;font-size:17px;color:var(--white)}
.nav .active{position:relative}
.nav .active::before{content:"";position:absolute;left:-6px;right:-6px;top:-34px;height:5px;background:var(--white)}
.hero-circle{left:418px;top:178px;width:372px;height:372px;border-radius:50%;background:#0a0f3d;box-shadow:0 0 40px rgba(0,0,0,.4);text-align:center;color:var(--white)}
.hero-circle h1{margin-top:95px;font-size:38px;line-height:42px;font-weight:700;letter-spacing:1px}
.hero-circle h1 span{font-weight:400;display:block}
.btn{display:inline-block;border-radius:30px;font-family:"Poppins",sans-serif;font-weight:500;color:var(--white);text-align:center}
.btn-hero{margin-top:22px;background:var(--sky);width:174px;height:48px;line-height:48px;font-size:17px}
.dots{display:flex;gap:7px;align-items:center}
.dots i{width:10px;height:10px;border-radius:50%;background:#cfd6e6;display:block}
.dots i.on{background:var(--white);width:12px;height:12px}
.dots b{width:20px;height:20px;border-radius:50%;background:var(--white);display:block}

/* About */
.section-title{font-size:40px;color:var(--ink)}
.about-title{left:130px;top:790px}
.about-copy{left:130px;top:862px;width:440px;font-size:16.5px;line-height:26px;color:var(--muted)}
.about-copy p{margin-bottom:16px}
.btn-blue{background:var(--azure);width:172px;height:48px;line-height:48px;font-size:17px}
.about-btn{left:130px;top:1056px}
.about-art{left:598px;top:764px;width:466px;height:326px;border-radius:12px;background:linear-gradient(135deg,#e7effb,#c6dcf5 50%,#9fc4ef)}

/* Services */
.services{left:0;top:1192px;width:1200px;height:512px;background:var(--light)}
.services-title{left:0;top:1244px;width:1200px;text-align:center;font-size:34px}
.svc{width:304px;height:304px;border-radius:50%;text-align:center;padding:62px 32px 0;color:var(--white)}
.svc h3{font-size:19px;line-height:25px;font-weight:500;margin-top:16px}
.svc p{font-size:12px;line-height:16px;margin-top:10px;opacity:.85}
.svc-a{left:181px;top:1312px;background:var(--navy)}
.svc-b{left:452px;top:1312px;background:var(--white);color:var(--royal);box-shadow:0 6px 24px rgba(0,0,0,.15)}
.svc-b p{color:var(--muted)}
.svc-c{left:744px;top:1312px;background:var(--azure)}
.chev{margin:14px auto 0;width:40px;height:40px;border-radius:50%;border:2px solid currentColor;display:flex;align-items:center;justify-content:center}

/* Projects */
.projects{left:0;top:1704px;width:1200px;height:472px;background:linear-gradient(135deg,#0a1f86,#124ec9 60%,#1b6fe0)}
.projects-title{left:0;top:1758px;width:1200px;text-align:center;font-size:34px;color:var(--white)}
.project{width:478px;height:218px;display:flex;background:rgba(40,130,240,.85)}
.project .photo{width:234px;height:218px;flex:none}
.project .body{padding:28px 24px;color:var(--white)}
.project h3{font-size:20px;font-weight:500}
.project p{font-size:12.5px;line-height:18px;margin-top:10px;opacity:.9}
.project .more{font-family:"Poppins",sans-serif;font-size:12px;font-weight:600;margin-top:12px;display:block}
.project-1{left:111px;top:1836px}
.project-2{left:610px;top:1836px}
.photo-1{background:linear-gradient(135deg,#c9b79a,#6d7380 60%,#3d4452)}
.photo-2{background:linear-gradient(135deg,#2b3340,#4b5b70 50%,#1b2230)}

/* Development team */
.devteam{left:0;top:2178px;width:1200px;height:504px;background:var(--pale)}
.dev-photo{left:0;top:2178px;width:676px;height:504px;background:linear-gradient(120deg,#d9dde3,#9aa3ae 50%,#4d5560)}
.dev-title{left:681px;top:2280px;font-size:36px}
.dev-copy{left:681px;top:2346px;width:400px;font-size:16.5px;line-height:26px;color:var(--muted)}
.dev-copy p{margin-bottom:14px}
.btn-navy{background:var(--navy);width:172px;height:48px;line-height:48px;font-size:17px}
.dev-btn{left:681px;top:2516px}

/* Testimonials */
.clients{left:28px;top:2690px;width:1144px;height:472px;background:#f7f8fa}
.clients-title{left:0;top:2750px;width:1200px;text-align:center;font-size:30px;color:var(--navy)}
.quote-stack{left:322px;top:2836px;width:608px;height:284px;background:#eceef2;border-radius:4px;box-shadow:0 2px 6px rgba(0,0,0,.12)}
.quote-card{left:312px;top:2822px;width:598px;height:292px;background:var(--white);border-radius:4px;box-shadow:0 2px 10px rgba(0,0,0,.18)}
.avatar{left:578px;top:2854px;width:68px;height:68px;border-radius:50%;background:linear-gradient(160deg,#cfd3d8,#8b939d)}
.quote-text{left:384px;top:2932px;width:456px;text-align:center;font-style:italic;font-size:15.5px;line-height:27px;color:var(--muted)}
.qmark{font-family:Georgia,serif;font-size:52px;color:var(--navy);font-weight:700;line-height:1}
.stars{left:538px;top:3016px;color:var(--star);font-size:22px;letter-spacing:4px}
.author{left:312px;top:3058px;width:598px;text-align:center;font-family:"Poppins",sans-serif;font-size:16px;font-weight:600;color:var(--ink)}
.arrow{top:2946px}

/* CTA */
.cta{left:0;top:3193px;width:1200px;height:385px;background:linear-gradient(90deg,rgba(20,24,32,.92),rgba(40,44,52,.78) 50%,rgba(20,24,32,.9)),linear-gradient(135deg,#3a3f48,#6a717c)}
.cta-title{left:0;top:3288px;width:1200px;text-align:center;font-size:34px;color:var(--white);letter-spacing:.5px}
.cta-copy{left:250px;top:3350px;width:700px;text-align:center;font-size:18px;line-height:26px;color:#e6e8ec}
.cta-btn{left:524px;top:3420px;background:var(--sky);width:186px;height:50px;line-height:50px}

/* Footer */
.footer{left:0;top:3578px;width:1200px;height:331px;background:linear-gradient(135deg,#0a1a82,#0c238f 60%,#0a1877)}
.fcol{top:3630px;color:var(--white)}
.fcol h4{font-family:"Poppins",sans-serif;font-weight:500;font-size:20px;margin-bottom:20px}
.fcol a{display:block;font-size:14px;line-height:32px;color:#c9d3f2;text-decoration:none}
.social{display:flex;gap:8px}
.social i{display:block;width:32px;height:32px;border-radius:50%;border:2px solid var(--white)}
.bottom{left:0;top:3909px;width:1200px;height:65px;background:var(--deep);text-align:center;line-height:65px;font-size:13px;color:#8592c4}
</style>
</head>
<body>

<header>
  <div class="abs hero" role="img" aria-label="Glowing blue digital background for the data platform banner"></div>
  <div class="abs hero-glow"></div>
  <svg class="abs" style="left:0;top:0" width="1200" height="720" aria-hidden="true">
    <path d="M0 620 L90 630 L210 660 L390 675 L540 650 L604 720 L700 670 L860 690 L1000 650 L1130 630 L1200 620 L1200 720 L0 720 Z" fill="#ffffff"/>
    <g fill="#ffffff" stroke="#1a5fd6" stroke-width="2">
      <circle cx="88" cy="630" r="6"/><circle cx="210" cy="660" r="6"/><circle cx="392" cy="675" r="6"/>
      <circle cx="700" cy="672" r="6"/><circle cx="822" cy="672" r="6"/><circle cx="1128" cy="631" r="6"/>
    </g>
  </svg>
  <div class="abs brand">Brivolan</div>
  <nav class="abs nav">
    <span class="active">Home</span><span>About</span><span>Services</span><span>Solution</span><span>Why Us</span><span>Support</span><span>Contact</span>
  </nav>
  <div class="abs hero-circle">
    <h1>DATA<br>PLATFORM<span>MANAGEMENT</span></h1>
    <span class="btn btn-hero">Get Started</span>
  </div>
  <div class="abs dots" style="left:548px;top:638px"><b></b><i class="on"></i><i></i><i></i><i></i><b></b></div>
</header>

<section>
  <h2 class="abs section-title about-title">About Brivolan</h2>
  <div class="abs about-copy">
    <p>Praesent elementum elit at tellus nec ultricies sit amet porttitor mattis enim In massa libero interdum nec</p>
    <p>interdum vel blandit sed nulla In ullamcorper est eget tempor cursus neque mi consectetuer mi a ultricies massa est sed nisl Class aptent taciti sociosqu ad litora torquent per conubia nostra per inceptos</p>
  </div>
  <span class="abs btn btn-blue about-btn">Learn More</span>
  <div class="abs about-art" role="img" aria-label="Isometric illustration of database servers, a laptop, a satellite and analytics dashboards"></div>
</section>

<section>
  <div class="abs services"></div>
  <svg class="abs" style="left:0;top:1192px" width="1200" height="20" aria-hidden="true">
    <path d="M588 0 L620 0 L604 14 Z" fill="#ffffff"/>
  </svg>
  <h2 class="abs services-title">Our Services</h2>

  <div class="abs svc svc-a">
    <svg width="62" height="62" viewBox="0 0 62 62" fill="none" stroke="#fff" stroke-width="2" aria-hidden="true"><circle cx="31" cy="31" r="13"/><circle cx="31" cy="31" r="5"/><path d="M31 6v8M31 48v8M6 31h8M48 31h8M13 13l6 6M43 43l6 6M13 49l6-6M43 19l6-6"/></svg>
    <h3>Administration and Development</h3>
    <p>Morbi diam mauris viverra in gravida eu mattis in ante Morbi</p>
    <div class="chev"><svg width="16" height="10" viewBox="0 0 16 10" fill="none" stroke="currentColor" stroke-width="2"><path d="M2 2l6 6 6-6"/></svg></div>
  </div>
  <div class="abs svc svc-b">
    <svg width="62" height="62" viewBox="0 0 62 62" fill="none" stroke="#1a5fd6" stroke-width="2" aria-hidden="true"><rect x="8" y="10" width="46" height="30" rx="3"/><path d="M24 48h14M31 40v8"/><rect x="16" y="18" width="30" height="6"/><rect x="16" y="27" width="30" height="6"/></svg>
    <h3>Database Operations</h3>
    <p>Morbi diam mauris viverra in gravida eu mattis in ante Morbi</p>
    <div class="chev" style="color:#8a93a3"><svg width="16" height="10" viewBox="0 0 16 10" fill="none" stroke="currentColor" stroke-width="2"><path d="M2 2l6 6 6-6"/></svg></div>
  </div>
  <div class="abs svc svc-c">
    <svg width="62" height="62" viewBox="0 0 62 62" fill="none" stroke="#fff" stroke-width="2" aria-hidden="true"><circle cx="31" cy="16" r="7"/><path d="M18 34c0-7 6-11 13-11s13 4 13 11"/><circle cx="14" cy="40" r="5"/><circle cx="48" cy="40" r="5"/><path d="M5 54c0-5 4-8 9-8s9 3 9 8M39 54c0-5 4-8 9-8s9 3 9 8"/></svg>
    <h3>Consult and Train the personnel responsible</h3>
    <p>Morbi diam mauris viverra in gravida eu mattis in ante Morbi</p>
    <div class="chev"><svg width="16" height="10" viewBox="0 0 16 10" fill="none" stroke="currentColor" stroke-width="2"><path d="M2 2l6 6 6-6"/></svg></div>
  </div>
</section>

<section>
  <div class="abs projects"></div>
  <h2 class="abs projects-title">Recent Projects</h2>
  <article class="abs project project-1">
    <div class="photo photo-1" role="img" aria-label="Photo of colleagues collaborating at a laptop"></div>
    <div class="body"><h3>Project Title here</h3><p>Class aptent taciti sociosqu ad litora torquent per conubia nostra per inceptos hymen aeos Proin nulla arcu</p><span class="more">READ MORE</span></div>
  </article>
  <article class="abs project project-2">
    <div class="photo photo-2" role="img" aria-label="Photo of hands working on a laptop keyboard"></div>
    <div class="body"><h3>Project Title here</h3><p>Class aptent taciti sociosqu ad litora torquent per conubia nostra per inceptos hymen aeos Proin nulla arcu</p><span class="more">READ MORE</span></div>
  </article>
  <div class="abs dots" style="left:552px;top:2100px"><b></b><i class="on"></i><i></i><i></i><i></i><b></b></div>
</section>

<section>
  <div class="abs devteam"></div>
  <div class="abs dev-photo" role="img" aria-label="Photo of a development team reviewing charts on a laptop in an office"></div>
  <h2 class="abs section-title dev-title">Development Team</h2>
  <div class="abs dev-copy">
    <p>Praesent elementum elit at tellus nec ultricies sit amet porttitor mattis enim In massa libe</p>
    <p>interdum vel blandit sed nulla In ullamcorper est eget tempor cursus neque mi consectetuer mi a ultricies massa est sed nisl Class aptent tac</p>
  </div>
  <span class="abs btn btn-navy dev-btn">Learn More</span>
</section>

<section>
  <div class="abs clients"></div>
  <h2 class="abs clients-title">What Our Client Says</h2>
  <svg class="abs arrow" style="left:240px" width="18" height="34" viewBox="0 0 18 34" fill="none" stroke="#777" stroke-width="3" aria-hidden="true"><path d="M16 2L3 17l13 15"/></svg>
  <svg class="abs arrow" style="left:952px" width="18" height="34" viewBox="0 0 18 34" fill="none" stroke="#777" stroke-width="3" aria-hidden="true"><path d="M2 2l13 15L2 32"/></svg>
  <div class="abs quote-stack"></div>
  <div class="abs quote-card"></div>
  <div class="abs avatar" role="img" aria-label="Client portrait"></div>
  <span class="abs qmark" style="left:336px;top:2914px">“</span>
  <span class="abs qmark" style="left:852px;top:2986px">”</span>
  <p class="abs quote-text">Class aptent taciti sociosqu ad litora torquent per conubia nostra per inceptos hymenaeos Proin nulla arcu nonummy luctus dictum eget fermentum et lorem</p>
  <div class="abs stars">★★★★</div>
  <p class="abs author">By Author Name, City Loction</p>
</section>

<section>
  <div class="abs cta" role="img" aria-label="Darkened photo of a person working at a computer screen"></div>
  <h2 class="abs cta-title">Get Started Data Management</h2>
  <p class="abs cta-copy">Praesent elementum elit at tellus nec ultricies sit amet porttitor mattis enim In massa libe interdum vel blandit sed nulla In ullamcorper</p>
  <span class="abs btn cta-btn">Learn More</span>
</section>

<footer>
  <div class="abs footer"></div>
  <div class="abs fcol" style="left:138px"><h4>Company</h4><a>Home</a><a>Our Services</a><a>Solution</a><a>Why Us</a><a>Team</a></div>
  <div class="abs fcol" style="left:321px"><h4>About</h4><a>About</a><a>Support</a><a>Testimonials</a><a>Privacy &amp; Terms</a></div>
  <div class="abs fcol" style="left:530px"><h4>Sublinks</h4><a>Lorem ipsum</a><a>Dolor sit</a><a>Amet consectet</a><a>Adipiscing elit</a><a>Nam cursus</a></div>
  <div class="abs fcol" style="left:726px"><h4>Resources</h4><a>Mauris vel</a><a>Aacus vitae felis</a><a>Vestibulum volut</a><a>Contact Us</a></div>
  <div class="abs fcol" style="left:917px"><h4>Follow Us</h4><div class="social"><i></i><i></i><i></i><i></i></div></div>
  <div class="abs bottom">© 2018 Company Name. All right reserved. Term of Use</div>
</footer>

</body>
</html>
```